依頼概要
■依頼の目的/概要
薬局で作っているかぜ薬の販促用のポスターを作成して頂きたいです。

■依頼詳細
以下の4つの文言と当社の社長の写真を入れたポスターのデザインをお願いします。

・私が毎日心を込めて作っております(キャッチコピー)
・薬剤師手作りのかぜ薬(キャッチコピーの下に一回り小さい文字でいれる)
・一度飲んだら手放せなくなります
・特に仕事で忙しくて病院に行けない方はご家庭に必携です
・社長の写真

薬局内に掲示するポスターになります。
実際に掲示するポスターのサイズはA0サイズで考えていますが、デザインはA4サイズでの作成をお願いいたします。
※社長の写真は添付ファイルにてご確認ください。

その他何かご不明な点がございましたら、お気軽にご質問下さい。
よろしくお願いいたします。
ポスター内の文字に関して、縦書きなら縦書き、横書きなら横書きに統一をお願いいたします。

仕事で忙しい方にも目にとまるようなデザインだったので、選ばせていただきました。

提案していただいたランサーの皆さん、ありがとうございました。

```html
<!DOCTYPE html>
<html lang="ja">
<head>
<meta charset="utf-8">
<title>薬剤師手作りのかぜ薬 ポスター</title>
<link rel="stylesheet" href="https://fonts.googleapis.com/css2?family=Noto+Serif+JP:wght@500;600&display=swap">
<style>
  :root {
    --band-green: #7f9a35;
    --band-light: rgba(214, 224, 168, 0.88);
    --text-white: #ffffff;
    --text-green: #55701c;
    --text-dark: #2a2a2a;
    --photo-light: #eceae4;
    --photo-mid: #b9aea0;
    --photo-dark: #6d6358;
    --photo-blue: #8f9bb0;
  }
  html, body {
    margin: 0;
    padding: 0;
    overflow: hidden;
    background: #ffffff;
  }
  .poster {
    position: relative;
    width: 847px;
    height: 1200px;
    overflow: hidden;
    font-family: "Noto Serif JP", serif;
  }
  .portrait {
    position: absolute;
    inset: 0;
    background:
      radial-gradient(ellipse 300px 280px at 120px 1040px, rgba(250, 249, 246, 0.97), rgba(250, 249, 246, 0) 100%),
      radial-gradient(ellipse 260px 220px at 400px 1000px, var(--photo-blue), rgba(143, 155, 176, 0) 100%),
      radial-gradient(ellipse 300px 380px at 440px 420px, #c9a58a, rgba(201, 165, 138, 0) 100%),
      radial-gradient(ellipse 360px 200px at 420px 60px, var(--photo-dark), rgba(109, 99, 88, 0) 100%),
      linear-gradient(100deg, var(--photo-light) 0%, var(--photo-mid) 55%, #9a9185 100%);
  }
  .band-main {
    position: absolute;
    left: 700px;
    top: 0;
    width: 119px;
    height: 1128px;
    background: var(--band-green);
  }
  .band-sub {
    position: absolute;
    left: 580px;
    top: 268px;
    width: 120px;
    height: 860px;
    background: var(--band-light);
  }
  .catchcopy {
    position: absolute;
    left: 722px;
    top: 28px;
    margin: 0;
    writing-mode: vertical-rl;
    font-size: 65px;
    font-weight: 600;
    line-height: 1.15;
    letter-spacing: 0;
    color: var(--text-white);
  }
  .subcopy {
    position: absolute;
    left: 615px;
    top: 296px;
    margin: 0;
    writing-mode: vertical-rl;
    font-size: 44px;
    font-weight: 600;
    line-height: 1.15;
    color: var(--text-green);
  }
  .body-copy {
    position: absolute;
    left: 130px;
    top: 822px;
    margin: 0;
    writing-mode: vertical-rl;
    font-size: 22.5px;
    font-weight: 500;
    line-height: 1.75;
    color: var(--text-dark);
  }
</style>
</head>
<body>
  <main class="poster">
    <div class="portrait" role="img" aria-label="手元のかぜ薬を見つめながら調合する薬剤師の社長のポートレート写真"></div>
    <div class="band-main"></div>
    <div class="band-sub"></div>
    <h1 class="catchcopy">私が毎日心を込めて作っております</h1>
    <h2 class="subcopy">薬剤師手作りのかぜ薬</h2>
    <p class="body-copy">一度飲んだら手放せなくなります<br>特に仕事で忙しくて病院に<br>行けない方はご家庭に必携です</p>
  </main>
</body>
</html>
```